Wine Bottle Label

Project: New Label for Kestrel Wine

Sponsored by: Nine Orchards (nineorchards.example and Marlowe Wines, producer of Kestrel Wines)

Product Description:

Wine comes in both red (cabernet, zinfandel) and white (Chardonnay, Sauvignon Blanc). It is marketed to restaurants and mid priced retailers including Fresh Basket, etc.) Wine is priced between $17 - $20 per bottle. The wine is in the medium price category and is intended for mid market appeal.

_
Label Requirements:

• Noticeable among other labels when on a black bottle. White labels are most noticeable but all color choices are an option if the brand stands out and can be easily recognizable from 10 – 12ft.

• Has to appeal to Gen X - younger people. Contemporary. Must appeal to women who buy the majority of wine in the US.

• Has to be presentable at the dinner table...slightly sophisticated.

• Has to connect with the “Official Emblem of the Larkfield Nature League” Great White Kestrel

• Bird is most often seen in grassy green pasture/meadows or wading in shallow water. Alone or in group.

• Has to fit on the bottle: Label size: 3 ½” H – 2 ¾” W

• Keep it Simple, lots of empty space

• Could be free form graphic design, illustrations, photos, etc.

• Could be abstract representation providing it connects to Egrets, e.g. stamp of foot which is gold embossed or similar.)

• Label must contain:

o Brand Name: Kestrel
o Varietal: will vary (Cabernet Sauvignon, Chardonnay, Sauvignon Blanc, Zinfandel, etc.)
o Appellation: varies (Sonoma County, Napa Valley, California)
o Vintage: 2010, 2011, etc.

• Variations in label color/design are possible between varietals but brand should be consistent.

Back design must also be included. Example of current back with text is attached.

Industry/Entity Type

Graphic Design

Requirements
Must have
• Must have relationship with Kestrel Bird - figuratively or literally
Has to fit on the bottle: Label size: 3 ½” H – 2 ¾” W
o Brand Name: Kestrel

```html
<!DOCTYPE html>
<html lang="en">
<head>
<meta charset="utf-8">
<title>Kestrel Wine – Cabernet Label</title>
<link rel="stylesheet" href="https://fonts.googleapis.com/css2?family=Cormorant+Garamond:ital,wght@0,400;0,500;1,400&display=swap">
<style>
  :root {
    --backdrop: #e8e6e2;
    --label-black: #0c0c0c;
    --label-sheen: #1c1c1c;
    --silver: #c9c9c9;
    --ivory: #ecebe6;
    --gold: #d9cfa6;
    --wine-red: #8f1a1f;
  }
  * { margin: 0; padding: 0; box-sizing: border-box; }
  html, body {
    width: 1200px;
    height: 782px;
    overflow: hidden;
    background: var(--backdrop);
  }
  .canvas {
    position: relative;
    width: 1200px;
    height: 782px;
  }
  .label {
    position: absolute;
    left: 350px;
    top: 20px;
    width: 500px;
    height: 742px;
    border-radius: 18px;
    background: linear-gradient(90deg, var(--label-black) 0%, var(--label-sheen) 45%, var(--label-black) 70%, var(--label-black) 100%);
    font-family: "Cormorant Garamond", "Times New Roman", serif;
    overflow: hidden;
  }
  .moon {
    position: absolute;
    left: 65px;
    top: 14px;
    width: 82px;
    height: 82px;
    border-radius: 50%;
    background: var(--gold);
  }
  .bird-art {
    position: absolute;
    left: 160px;
    top: 0;
    width: 200px;
    height: 340px;
    background: linear-gradient(180deg, rgba(217,207,166,0.08), rgba(217,207,166,0.22));
  }
  .horizon {
    position: absolute;
    left: 50px;
    top: 330px;
    width: 380px;
    height: 60px;
  }
  .brand {
    position: absolute;
    left: 0;
    width: 420px;
    top: 378px;
    text-align: center;
    font-size: 104px;
    font-weight: 400;
    color: var(--silver);
    line-height: 1;
  }
  .vintage {
    position: absolute;
    left: 0;
    width: 420px;
    top: 532px;
    text-align: center;
    font-size: 34px;
    color: var(--wine-red);
    letter-spacing: 1px;
  }
  .appellation {
    position: absolute;
    left: 0;
    width: 430px;
    top: 590px;
    text-align: center;
    font-size: 30px;
    font-weight: 500;
    color: var(--ivory);
    letter-spacing: 1px;
  }
  .varietal {
    position: absolute;
    left: 0;
    width: 430px;
    top: 632px;
    text-align: center;
    font-size: 44px;
    color: var(--wine-red);
    letter-spacing: 3px;
  }
  .fine-print {
    position: absolute;
    top: 712px;
    font-size: 15px;
    color: var(--ivory);
    letter-spacing: 0.5px;
  }
  .fine-print--alcohol { left: 36px; }
  .fine-print--volume { right: 44px; }
</style>
</head>
<body>
  <main class="canvas">
    <section class="label">
      <div class="moon"></div>
      <div class="bird-art" role="img" aria-label="Line illustration of a white kestrel standing beneath the moon"></div>
      <svg class="horizon" viewBox="0 0 380 60" aria-hidden="true">
        <path d="M0 32 Q 170 0 380 48" fill="none" stroke="var(--gold)" stroke-width="2"/>
      </svg>
      <h1 class="brand">Kestrel</h1>
      <p class="vintage">2010</p>
      <p class="appellation">NAPA VALLEY</p>
      <p class="varietal">CABERNET</p>
      <p class="fine-print fine-print--alcohol">ALC 13.5% BY VOL</p>
      <p class="fine-print fine-print--volume">750 ML</p>
    </section>
  </main>
</body>
</html>
```